DL Flyer Design

I need a DL flyer, double-sided designed for a Brisbane based outdoor group exercise/training company called Move Ahead! Move Ahead! provides group outdoor training, designed for the individual. It provides the support, motivation and one-on-one attention of personal training combined with the support of a group environment. The classes are fun, challenging and aim to develop confidence & fitness. Weight loss is not the focus, although it is a benefit.
Updates

Hi

I've just uploaded a high res version of the logo if you need.

Cheers
Tam

Target Market(s)

English speaking men & women aged 25 - 45, white-collar office jobs. Average-low level of fitness, not hugely 'fitness' oriented but want to improve quality of life, overall fitness, lose a bit of weight.

Computer and consumer literate. Live in suburban Brisbane, Australia.

Industry/Entity Type

Training

Requirements
Must have
• Double sided DL. Use of black, greens and white per attached photos. Use of 1300 572 914 (1300 RUN FAR) and website www.movaheadactive.com.au

Indicative copy and contents is posted in the comments section.

```html
<!DOCTYPE html>
<html lang="en">
<head>
<meta charset="utf-8">
<title>Move Ahead! DL Flyer</title>
<link rel="stylesheet" href="https://fonts.googleapis.com/css2?family=Archivo+Black&family=Arimo:wght@400;700&display=swap">
<style>
  :root {
    --black: #000000;
    --white: #ffffff;
    --green-deep: #12bf45;
    --green-mid: #6cc23a;
    --green-lime: #a3cf45;
    --green-text: #1fbf4b;
    --orange: #ff6a00;
    --ink: #2b2b2b;
    --panel: rgba(255,255,255,0.55);
  }
  * { box-sizing: border-box; margin: 0; padding: 0; }
  html, body { width: 1200px; height: 901px; overflow: hidden; background: var(--white); }
  .stage {
    position: relative; width: 1200px; height: 901px;
    background: var(--black); border-radius: 44px; overflow: hidden;
    font-family: "Arimo", Arial, sans-serif;
  }
  .flyer {
    position: absolute; width: 723px; height: 362px; overflow: hidden;
    background: linear-gradient(100deg, var(--green-deep) 0%, var(--green-mid) 35%, var(--green-lime) 70%, #9ccb45 100%);
  }
  .flyer--front { left: 240px; top: 75px; }
  .flyer--back  { left: 237px; top: 464px; }
  .runner-art {
    position: absolute; right: 0; top: 0; width: 420px; height: 362px;
    background: radial-gradient(ellipse at 70% 40%, rgba(255,255,255,0.55), rgba(255,255,255,0) 65%);
  }
  .abs { position: absolute; white-space: nowrap; }
  .center { transform: translateX(-50%); text-align: center; }
  .brand {
    font-family: "Archivo Black", "Arial Black", sans-serif; color: var(--white);
    display: flex; align-items: center; gap: 8px; line-height: 1;
  }
  .brand-dot { width: 18px; height: 18px; border-radius: 50%; background: var(--black); flex: none; }
  .tagline {
    font-family: "Archivo Black", "Arial Black", sans-serif; color: var(--green-text);
    -webkit-text-stroke: 1px var(--white); paint-order: stroke fill;
    text-shadow: 0 0 2px #fff, 0 0 2px #fff;
  }
  .tagline--cta { color: var(--orange); }
  .phone {
    font-family: "Archivo Black", "Arial Black", sans-serif; color: var(--white);
    text-shadow: -2px 0 #000, 2px 0 #000, 0 -2px #000, 0 2px #000, 1px 1px #000, -1px -1px #000;
    line-height: 1;
  }
  .contact {
    font-family: "Arimo", Arial, sans-serif; font-weight: 700; color: var(--white);
    text-shadow: -1px 0 #000, 1px 0 #000, 0 -1px #000, 0 1px #000;
  }
  .info-panel {
    position: absolute; left: 325px; top: 22px; width: 376px; height: 320px;
    border-radius: 26px; background: var(--panel); border: 1px solid rgba(255,255,255,0.8);
  }
  .info-title { font-weight: 700; font-size: 18px; color: var(--ink); }
  .info-body { font-size: 10px; color: var(--ink); line-height: 13px; white-space: normal; width: 270px; }
  .info-strong { font-weight: 700; font-size: 11px; color: var(--ink); line-height: 16px; white-space: normal; width: 300px; }
  .offer { font-family: "Archivo Black", "Arial Black", sans-serif; color: var(--green-text); }
  .offer-sub { font-size: 17px; color: var(--green-text); }
  .offer-hot { font-family: "Archivo Black", "Arial Black", sans-serif; color: var(--orange); font-size: 25px; line-height: 28px; }
  .guarantee { position: absolute; left: 551px; top: 203px; width: 128px; height: 128px; }
  .guarantee-text {
    position: absolute; inset: 0; display: flex; flex-direction: column; align-items: center; justify-content: center;
    font-size: 13px; color: var(--ink); line-height: 14px; text-align: center;
  }
  .guarantee-text b { font-size: 13px; }
  .program-panel {
    position: absolute; left: 25px; top: 127px; width: 673px; height: 216px;
    border-radius: 18px; background: rgba(255,255,255,0.72); border: 1px solid rgba(255,255,255,0.9);
  }
  .program-title { font-weight: 700; font-size: 28px; color: var(--ink); }
  .day { font-size: 16px; color: var(--ink); }
  .slot { font-size: 10px; font-weight: 700; color: #333; line-height: 11px; text-align: center; }
  .slot--time { color: var(--orange); }
  .divider { position: absolute; width: 1px; background: #555; top: 71px; height: 133px; }
  .private-bar {
    position: absolute; left: 561px; top: 115px; width: 112px; height: 26px; background: var(--orange);
    color: var(--white); font-size: 10px; font-weight: 700; line-height: 10px; text-align: center; padding-top: 3px;
  }
</style>
</head>
<body>
<main class="stage">

  <section class="flyer flyer--front">
    <div class="runner-art" role="img" aria-label="Large faint white silhouette of a leaping runner"></div>

    <div class="abs brand center" style="left:160px; top:82px; font-size:34px;"><span class="brand-dot"></span>Move Ahead!</div>
    <div class="abs tagline center" style="left:164px; top:160px; font-size:20px;">Tired of hanging about?</div>
    <div class="abs tagline tagline--cta center" style="left:164px; top:186px; font-size:25px;">.....Just Move Ahead!</div>
    <div class="abs phone center" style="left:164px; top:230px; font-size:29px;">1300 RUN FAR</div>
    <div class="abs phone center" style="left:164px; top:260px; font-size:29px;">1300 572 914</div>
    <div class="abs contact center" style="left:164px; top:293px; font-size:15px;">hello@movaheadactive.com.au</div>
    <div class="abs contact center" style="left:164px; top:313px; font-size:15px;">www.movaheadactive.com.au</div>

    <div class="info-panel">
      <div class="abs info-title" style="left:27px; top:17px;">It's time to Move Ahead!</div>
      <div class="abs info-body" style="left:27px; top:40px;">with group outdoor training, designed just for you.</div>
      <div class="abs info-title" style="left:27px; top:67px;">Move Ahead!</div>
      <div class="abs info-body" style="left:27px; top:89px;">provides the unique combination of the one-on-one attention of personal training with the motivation and support of a group environment.</div>
      <div class="abs info-strong" style="left:27px; top:141px;">Best of all, it's designed to fit fitness into your life<br><span style="font-size:12px;">@ an affordable price.</span></div>
      <div class="abs offer center" style="left:118px; top:185px; font-size:23px;">Curious???</div>
      <div class="abs offer-sub center" style="left:118px; top:213px;">Give it a shot with a</div>
      <div class="abs offer-hot center" style="left:118px; top:240px;">1week<br>free trial!</div>
    </div>

    <div class="guarantee">
      <svg width="128" height="128" viewBox="0 0 128 128" aria-hidden="true">
        <defs>
          <radialGradient id="burstFill" cx="45%" cy="40%" r="65%">
            <stop offset="0%" stop-color="#f2ffb8"/>
            <stop offset="100%" stop-color="#9fd23a"/>
          </radialGradient>
        </defs>
        <polygon fill="url(#burstFill)" stroke="#7fae2c" stroke-width="1" points="64,4 72,16 86,9 89,24 104,22 101,37 116,42 107,54 119,64 107,74 116,86 101,91 104,106 89,104 86,119 72,112 64,124 56,112 42,119 39,104 24,106 27,91 12,86 21,74 9,64 21,54 12,42 27,37 24,22 39,24 42,9 56,16"/>
      </svg>
      <div class="guarantee-text"><b>Guaranteed</b>no hard sell<br>at the end</div>
    </div>
  </section>

  <section class="flyer flyer--back">
    <div class="runner-art" role="img" aria-label="Large faint white silhouettes of leaping runners"></div>

    <div class="abs brand" style="left:20px; top:48px; font-size:21px;"><span class="brand-dot" style="width:13px;height:13px;"></span>Move Ahead!</div>
    <div class="abs tagline center" style="left:340px; top:45px; font-size:19px;">Tired of hanging about?</div>
    <div class="abs tagline tagline--cta center" style="left:340px; top:70px; font-size:25px;">.....Just Move Ahead!</div>
    <div class="abs phone center" style="left:601px; top:36px; font-size:22px;">1300 RUN FAR</div>
    <div class="abs phone center" style="left:601px; top:59px; font-size:22px;">1300 572 914</div>
    <div class="abs contact center" style="left:601px; top:81px; font-size:13px;">hello@movaheadactive.com.au</div>
    <div class="abs contact center" style="left:601px; top:97px; font-size:13px;">www.movaheadactive.com.au</div>

    <div class="program-panel">
      <div class="abs program-title center" style="left:332px; top:14px;">Session Program</div>

      <div class="abs day center" style="left:66px; top:51px;">Time</div>
      <div class="abs day center" style="left:149px; top:51px;">Monday</div>
      <div class="abs day center" style="left:241px; top:51px;">Tuesday</div>
      <div class="abs day center" style="left:334px; top:51px;">Wednesday</div>
      <div class="abs day center" style="left:424px; top:51px;">Thursday</div>
      <div class="abs day center" style="left:517px; top:51px;">Friday</div>
      <div class="abs day center" style="left:613px; top:51px;">Saturday</div>

      <div class="divider" style="left:100px;"></div>
      <div class="divider" style="left:193px;"></div>
      <div class="divider" style="left:285px;"></div>
      <div class="divider" style="left:470px;"></div>
      <div class="divider" style="left:561px;"></div>

      <div class="abs slot slot--time center" style="left:66px; top:82px;">6.00am</div>
      <div class="abs slot center" style="left:144px; top:82px;">Cardio</div>
      <div class="abs slot center" style="left:333px; top:77px;">Stress-relief<br>(boxing)</div>
      <div class="abs slot center" style="left:420px; top:82px;">Cardio</div>
      <div class="abs slot center" style="left:519px; top:77px;">Stress-relief<br>(boxing)</div>
      <div class="abs slot slot--time center" style="left:615px; top:82px;">Mush-Up</div>
      <div class="private-bar">One-on-One<br>sessions</div>

      <div class="abs slot slot--time center" style="left:66px; top:165px;">6.00pm</div>
      <div class="abs slot center" style="left:149px; top:164px;">Strenght</div>
      <div class="abs slot center" style="left:239px; top:165px;">Cardio</div>
      <div class="abs slot center" style="left:333px; top:164px;">Strenght</div>
      <div class="abs slot center" style="left:425px; top:160px;">Stress-relief<br>(boxing)</div>
    </div>
  </section>

</main>
</body>
</html>
```